依頼詳細
・商品が増えたので新商品の案内 ギフト商品の紹介のチラシ(金額は入れません。)
・「こはるフルーツソース2本セット」を目玉として大きめに表示してください。
・商品の色を前面に出したデザインによる商品紹介
・文章はなるべく入れないで写真を強調した、シンプルでわかりやすいデザイン
・食品関連ギフトのチラシの作成経験者歓迎
・真空低温調理によるジャム製造のため、酸化も少なく、色が鮮やかなジャムに仕上がっています。
・自社農園産の果物を中心に、宮崎県産果物のみを使用。
・通常の手作業では実現できない品質をご提供することができます。
記載項目
「宝石のようなトロピカルジャム」という文言を必ず使用してください。

・こはるフルーツソース2本セット
「北海道産てんさい糖と宮崎県産フルーツのみを煮詰めたこだわりのソース」
内容:マンゴーソース  145g
パッションフルーツソース 145g

・こはるフルーツジャム6個セット
内容:マンゴージャム 150g
日向夏マーマレード 150g
きんかんマーマレード 150g
パイナップルジャム 150g
ブルーベリージャム 150g
パパイアジャム  150g

・こはるフルーツミニジャム6個セット
内容:マンゴージャム 50g
日向夏マーマレード 50g
きんかんマーマレード 50g
パイナップルジャム 50g
ブルーベリージャム 50g
パパイアジャム 50g

桐原白浜果樹株式会社
〒876-2231 宮崎県宮崎市桜丘町岩瀬2264番地
電話番号: 0985-47-2291
FAX:  0985-47-3356
サイズ
A4
ページ数
片面
希望イメージ
シンプル 複雑
単色 カラフル
暗い 明るい
日常 高級
遊び心 厳粛
未来的 伝統的
女性的 男性的
希望する色
納品ファイル
補足説明
■ 選んだ理由

シンプルで、しかも美味しさと高級感が伝わるようなデザインで、社内アンケートの結果一番評価が高かったので決めさせていただきました。

■ 提案者全員のお礼・コメント

たくさんのご提案をしていただき、選考には時間が
かかってしまい申し訳ありませんでした。どの方も素晴らしく、選ぶのにすごく悩みましたが、社内で検討し、一人の方を選ばせていただきました。
今回、初めて利用させていただきましたが、皆様のような素晴らしいデザイナーさんがいらっしゃるということが実感できましたので、また
利用させていただきたいと考えておりますので、今後ともどうぞよろしくお願いいたします。
本当にありがとうございました。

```html
<!DOCTYPE html>
<html lang="ja">
<head>
<meta charset="utf-8">
<title>宝石のようなトロピカルジャム</title>
<link rel="stylesheet" href="https://fonts.googleapis.com/css2?family=Noto+Serif+JP:wght@400;600;700;900&family=Great+Vibes&display=swap">
<style>
:root{
  --paper:#fbf8f2;
  --ink:#3a2a1e;
  --muted:#6d5a4a;
  --pink:#d6387e;
  --gold:#c9a96b;
  --orange:#ea7d12;
  --amber:#f0a21a;
  --green:#7aa62a;
  --lime:#b3c52b;
  --band:#3b2418;
  --band-text:#f4e6c8;
  --rule:#c7b79c;
}
*{margin:0;padding:0;box-sizing:border-box}
html,body{width:849px;height:1200px;overflow:hidden;background:var(--paper)}
body{font-family:"Noto Serif JP",serif;color:var(--ink);position:relative}
.flyer{position:absolute;inset:0;width:849px;height:1200px}
.abs{position:absolute;white-space:nowrap}

.title-gift{left:250px;top:50px;font-family:"Great Vibes",cursive;font-size:88px;color:var(--gold);opacity:.45;line-height:1}
.title-lead{left:70px;top:92px;font-size:40px;font-weight:600;color:var(--pink);letter-spacing:2px;line-height:1.2}
.title-main{left:30px;top:150px;font-size:82px;font-weight:900;letter-spacing:-4px;line-height:1}
.title-main .c1{color:var(--orange)}
.title-main .c2{color:var(--amber)}
.title-main .c3{color:var(--green)}
.title-main .c4{color:var(--lime)}
.title-main .c5{color:var(--orange)}
.title-sub{left:40px;top:244px;font-size:78px;font-weight:900;color:var(--amber);line-height:1;letter-spacing:2px}

.photo-jamset{left:470px;top:28px;width:362px;height:298px;background:linear-gradient(135deg,#2a1c14,#5a3a1e 45%,#d08a22 70%,#3a2418)}
.photo-minijam{left:470px;top:380px;width:362px;height:258px;background:linear-gradient(160deg,#e9e2d6,#c9462a 40%,#e0a030 65%,#efe9df)}
.photo-sauce{left:90px;top:345px;width:300px;height:540px;background:linear-gradient(90deg,#f1ece2 0%,#6a5a2c 20%,#d9a42a 38%,#efe7d8 50%,#f2a818 65%,#e78a10 80%,#f1ece2 100%)}
.photo-pancake{left:28px;top:950px;width:184px;height:190px;border-radius:50% 50% 8px 8px;background:radial-gradient(circle at 50% 45%,#f6d24a,#d8912f 55%,#8e5a2c 90%)}

.cap{font-size:15px;font-weight:600;color:var(--ink);line-height:1.4}
.cap .mark{color:var(--pink)}
.cap .weight{font-weight:400;color:var(--muted);margin-left:14px}
.cap-a{left:474px;top:336px;width:358px;display:flex;justify-content:space-between}
.cap-b{left:474px;top:648px;width:358px;display:flex;justify-content:space-between}
.contents{left:482px;top:690px;font-size:13.5px;line-height:1.8;color:var(--ink)}
.contents .head{color:var(--pink);font-weight:600}

.tagline{left:28px;top:345px;writing-mode:vertical-rl;font-size:14px;letter-spacing:2px;color:var(--muted)}
.cap-sauce{left:92px;top:896px;font-size:17px;font-weight:700}
.cap-sauce .weight{font-size:15px}
.cap-sauce-list{left:104px;top:924px;font-size:12.5px;color:var(--muted)}

.band{left:0;top:945px;width:849px;height:64px;background:var(--band)}
.band-text{left:230px;top:954px;font-size:24px;font-weight:700;color:var(--band-text);letter-spacing:1px;line-height:1.4}
.band-line{left:230px;top:996px;width:590px;height:1px;background:var(--gold)}
.lead{left:232px;top:1018px;width:590px;font-size:11.5px;line-height:1.7;color:var(--muted);white-space:normal}
.rule{left:232px;top:1064px;width:590px;height:1px;background:var(--rule)}
.company{right:28px;top:1074px;font-size:24px;font-weight:700;color:var(--ink);letter-spacing:2px;line-height:1.4}
.contact{right:28px;top:1116px;font-size:11.5px;color:var(--muted);text-align:right;line-height:1.5}
</style>
</head>
<body>
<main class="flyer">
  <div class="abs title-gift">Gift</div>
  <div class="abs title-lead">宝石のような</div>
  <h1 class="abs title-main"><span class="c1">ト</span><span class="c2">ロ</span><span class="c3">ピ</span><span class="c4">カ</span><span class="c5">ル</span></h1>
  <div class="abs title-sub">ジャム</div>

  <div class="abs photo-jamset" role="img" aria-label="化粧箱に並んだフルーツジャム6個セットの写真"></div>
  <div class="abs cap cap-a"><span><span class="mark">Ⓐ</span> こはるフルーツジャム6個セット</span><span class="weight">各150g</span></div>

  <div class="abs photo-minijam" role="img" aria-label="色とりどりのミニジャム6個セットの写真"></div>
  <div class="abs cap cap-b"><span><span class="mark">Ⓑ</span> こはるフルーツミニジャム6個セット</span><span class="weight">各50g</span></div>
  <div class="abs contents">
    <div class="head">Ⓐ Ⓑ 内容（共通）</div>
    <div>マンゴージャム・日向夏マーマレード</div>
    <div>ブルーベリージャム・パパイアジャム</div>
    <div>きんかんマーマレード・パイナップルジャム</div>
  </div>

  <div class="abs tagline">北海道産てんさい糖と宮崎県産フルーツのみを煮詰めたこだわりのソース</div>
  <div class="abs photo-sauce" role="img" aria-label="マンゴーとパッションフルーツのソース瓶2本の写真"></div>
  <div class="abs cap cap-sauce"><span class="mark">◆</span>こはるフルーツソース2本セット<span class="weight">各145g</span></div>
  <div class="abs cap-sauce-list">内容：マンゴーソース／パッションフルーツソース</div>

  <div class="abs band"></div>
  <div class="abs photo-pancake" role="img" aria-label="ソースをかけたパンケーキの写真"></div>
  <div class="abs band-text">通常の手作業では実現できない品質をご提供</div>
  <div class="abs band-line"></div>
  <p class="abs lead">自社農園産の果物を中心に、宮崎県産果物のみを使用。さらに、真空低温調理によるジャム製造のため、酸化も少なく、色が鮮やかなジャムに仕上がっています。</p>
  <div class="abs rule"></div>
  <div class="abs company">桐原白浜果樹株式会社</div>
  <div class="abs contact">〒876-2231 宮崎県宮崎市桜丘町岩瀬2264番地<br>TEL. 0985-47-2291　FAX. 0985-47-3356</div>
</main>
</body>
</html>
```